BQN - New Homepage needed for an existing website

Lantern of Meridel Website
Need a new Homepage for an existing website with Action Items and Newer Pictures
This is the current Website
https://lanternofmeridel.example/

This new page will be changed on Jan 21st when Voting begins
1. Voting like a political campaign where we are trying to raise awareness for the issues we stand for and urge the people to go to a Polling /voting website and vote for us (Roster 27)
2. We have 6 basic themes as to what we stand for - there will be text to promote their importance of voting/call to action
3. There will be videos on the website and there will be a simulation of how the voting process works - will be added later

Use colors like the US Flag - Red, White and Blue. The other pages don't need to be changed - only the HomePage.

I only need the design, I will code the website. Thank you

Target Market(s)

Jewish People in the US

Industry/Entity Type

Religious

Number of Pages Required

1 page

Font styles to use
Serif
Sans Serif

Colors

Designer to choose colors to be used in the design.

Requirements
Must have
• Call to Action - Go out to Vote
• This is the current Website - https://lanternofmeridel.example/

```html
<!DOCTYPE html>
<html lang="en">
<head>
<meta charset="utf-8">
<title>Lantern of Meridel — Homepage</title>
<link rel="stylesheet" href="https://fonts.googleapis.com/css2?family=Open+Sans:wght@400;600;700&display=swap">
<style>
:root{
  --red:#d0021b;
  --blue:#0a2db0;
  --blue-mid:#1b3fc4;
  --blue-light:#6b86dc;
  --black:#000;
  --white:#fff;
  --card:#d6d6d6;
  --form-bg:#eaf1ec;
  --text:#333;
}
*{box-sizing:border-box;margin:0;padding:0}
html,body{width:1200px;height:3356px;overflow:hidden;background:var(--white)}
body{font-family:"Open Sans",sans-serif;color:var(--text)}
.page{position:relative;width:1200px;height:3356px;overflow:hidden;background:var(--white)}
.abs{position:absolute}

/* header + hero */
.hero{position:absolute;left:0;top:0;width:1200px;height:600px;background:var(--black)}
.nav-link{position:absolute;top:42px;color:var(--white);font-size:13px;font-weight:600;letter-spacing:.2px}
.nav-rule{position:absolute;left:0;top:88px;width:1200px;height:1px;background:#444}
.brand-tri{position:absolute;left:495px;top:0;width:209px;height:128px}
.brand-name{position:absolute;left:545px;top:34px;width:110px;text-align:center;font-size:11px;font-weight:700;color:var(--black);line-height:13px}
.chev{display:inline-block;margin-left:4px;vertical-align:2px}
.hero-photo{position:absolute;left:221px;top:156px;width:352px;height:352px}
.hero-kicker{position:absolute;left:609px;top:210px;color:var(--white);font-size:26px;font-weight:600}
.hero-title{position:absolute;left:602px;top:246px;color:var(--red);font-size:40px;font-weight:700;letter-spacing:.3px}
.hero-sub{position:absolute;left:601px;top:307px;color:var(--white);font-size:17px;font-weight:600}
.pill{position:absolute;display:flex;align-items:center;justify-content:center;border-radius:20px;color:var(--white);font-weight:600}
.pill .arrow{position:absolute;right:9px;top:50%;transform:translateY(-50%)}
.btn-hero{width:297px;height:31px;font-size:13px;padding-right:20px}
.btn-red{background:var(--red)}
.btn-blue{background:var(--blue)}

/* mission */
.eyebrow{position:absolute;left:222px;top:760px;color:var(--blue);font-size:15px;font-weight:700}
.section-title{position:absolute;color:var(--red);font-size:29px;font-weight:700}
.mission-copy{position:absolute;left:222px;top:823px;width:470px;font-size:10.4px;line-height:13.8px;text-align:justify;color:#444}
.btn-small{height:30px;width:100px;font-size:9.5px;padding-right:20px}
.mission-frame{position:absolute;left:757px;top:732px;width:216px;height:296px;border:1.5px solid #222}
.mission-photo{position:absolute;left:766px;top:740px;width:214px;height:280px;background:linear-gradient(90deg,var(--blue) 0 50%,var(--red) 50% 100%)}
.mission-photo::after{content:"";position:absolute;left:40px;top:30px;width:150px;height:250px;border-radius:70px 70px 0 0;background:linear-gradient(#bdbdbd,#6e6e6e)}

/* pillars */
.pillar-map{position:absolute;left:330px;top:1070px;width:540px;height:370px}
.pillar-label{position:absolute;font-size:12.5px;font-weight:500;color:#222;text-align:center;line-height:15px}
.hex-name{position:absolute;left:539px;top:1262px;width:120px;text-align:center;color:var(--white);font-size:13px;font-weight:700;line-height:16px}

/* objectives */
.card{position:absolute;width:245px;height:207px;background:var(--card);text-align:center;padding:29px 16px 0}
.card.featured{background:var(--blue);color:var(--white)}
.card h3{font-size:12px;font-weight:700;color:#111;margin-bottom:10px}
.card.featured h3{color:var(--white)}
.card p{font-size:9.2px;line-height:13.2px;text-align:justify;text-align-last:center}
.card .btn-card{position:absolute;left:50%;bottom:28px;transform:translateX(-50%);width:94px;height:21px;border-radius:11px;background:var(--red);color:var(--white);font-size:8.5px;font-weight:700;display:flex;align-items:center;justify-content:center}

/* voting */
.vote-band{position:absolute;left:220px;top:2065px;width:759px;height:263px;background:var(--red)}
.vote-title{position:absolute;left:241px;top:2095px;color:var(--white);font-size:29px;font-weight:700}
.vote-video{position:absolute;left:238px;top:2156px;width:724px;height:320px;background:linear-gradient(120deg,#4a4e57 0%,#2f3a4a 45%,#7b6e62 75%,#c9c6c0 100%)}
.play{position:absolute;left:562px;top:2288px}

/* join form */
.join{position:absolute;left:222px;top:2491px;width:758px;height:443px;background:var(--form-bg)}
.join-title{position:absolute;left:0;top:2553px;width:1200px;text-align:center;color:var(--red);font-size:29px;font-weight:600}
.join-sub{position:absolute;left:0;top:2595px;width:1200px;text-align:center;font-size:13.5px;color:#333}
.field{position:absolute;background:var(--blue);color:var(--white);border-radius:18px;font-size:9px;padding-left:17px;display:flex;align-items:center}
.field.msg{align-items:flex-start;padding-top:18px;border-radius:26px}
.btn-vote{left:508px;top:2857px;width:184px;height:41px;font-size:16px;font-weight:500;padding-right:12px}
.btn-vote svg{margin-left:10px}

/* footer */
.footer-wave{position:absolute;left:0;top:2918px;width:1200px;height:142px}
.footer{position:absolute;left:0;top:3058px;width:1200px;height:298px;background:var(--black)}
.footer-brand{position:absolute;left:0;top:3182px;width:1200px;text-align:center;color:#5a5a5a;font-size:14px;font-weight:700;letter-spacing:.5px}
.footer-link{position:absolute;top:3260px;color:var(--white);font-size:11px;font-weight:600}
.footer-rule{position:absolute;left:222px;top:3310px;width:758px;height:1px;background:#333}
.copyright{position:absolute;left:0;top:3326px;width:1200px;text-align:center;color:var(--white);font-size:10.5px}
</style>
</head>
<body>
<div class="page">

  <!-- header & hero -->
  <header class="hero"></header>
  <a class="nav-link" style="left:222px">HOME</a>
  <a class="nav-link" style="left:326px">MISSION STATEMENT</a>
  <a class="nav-link" style="left:743px">OBJECTIVES<svg class="chev" width="9" height="6" viewBox="0 0 9 6"><path d="M1 1l3.5 3.5L8 1" stroke="#fff" stroke-width="1.4" fill="none"/></svg></a>
  <a class="nav-link" style="left:905px">CONTACT US</a>
  <div class="nav-rule"></div>
  <svg class="brand-tri" viewBox="0 0 209 128"><polygon points="0,0 209,0 104,128" fill="#fff"/></svg>
  <div class="brand-name">LANTERN OF MERIDEL</div>

  <svg class="hero-photo" viewBox="0 0 352 352" role="img" aria-label="Smiling woman giving a thumbs up, black and white portrait">
    <defs><linearGradient id="heroGrey" x1="0" y1="0" x2="1" y2="1"><stop offset="0" stop-color="#cfcfcf"/><stop offset="1" stop-color="#4d4d4d"/></linearGradient></defs>
    <circle cx="176" cy="176" r="176" fill="var(--red)"/>
    <circle cx="168" cy="162" r="166" fill="var(--black)"/>
    <circle cx="168" cy="150" r="150" fill="url(#heroGrey)"/>
  </svg>

  <div class="hero-kicker">IT'S ALL ABOUT</div>
  <div class="hero-title">JEWISH CONTINUITY</div>
  <div class="hero-sub">WE EMBRACE OUR PAST TO ENSURE OUR FUTURE</div>
  <a class="pill btn-hero btn-red" style="left:601px;top:353px">JOIN THE JEWISH FUTURE
    <svg class="arrow" width="19" height="19" viewBox="0 0 19 19"><circle cx="9.5" cy="9.5" r="8.5" fill="none" stroke="#fff" stroke-width="1.3"/><path d="M7 6l3.5 3.5L7 13M10 6l3.5 3.5L10 13" stroke="#fff" stroke-width="1.3" fill="none"/></svg></a>
  <a class="pill btn-hero btn-blue" style="left:599px;top:404px;width:301px">NEW LAW INCREASES HATE CRIMES
    <svg class="arrow" width="19" height="19" viewBox="0 0 19 19"><circle cx="9.5" cy="9.5" r="8.5" fill="none" stroke="#fff" stroke-width="1.3"/><path d="M7 6l3.5 3.5L7 13M10 6l3.5 3.5L10 13" stroke="#fff" stroke-width="1.3" fill="none"/></svg></a>

  <svg class="abs" style="left:0;top:540px" width="1200" height="160" viewBox="0 0 1200 160">
    <rect width="1200" height="160" fill="#fff"/>
    <path d="M0,100 C40,125 70,140 100,158 L0,158 Z" fill="var(--blue-light)"/>
    <path d="M880,25 C1040,15 1150,40 1200,60 V115 C1100,85 990,55 880,25 Z" fill="var(--blue-light)"/>
    <path d="M560,55 C700,10 850,0 1000,35 C1100,60 1170,85 1200,95 V150 C1100,140 950,110 800,92 C700,80 620,72 560,55 Z" fill="var(--blue-mid)"/>
    <path d="M0,0 H1200 V30 C1000,10 820,0 660,30 C460,70 300,160 160,150 C90,145 40,130 0,115 Z" fill="#000"/>
  </svg>

  <!-- mission -->
  <div class="eyebrow">MISSION STATEMENT</div>
  <h1 class="section-title" style="left:222px;top:778px">LANTERN OF MERIDEL</h1>
  <p class="mission-copy">Lantern of Meridel is a grassroots movement that was established to promote Jewish Continuity, recognizing that in the United States, Judaism and its continuity are under attack for a host of reasons, all of which Lantern of Meridel believes must be identified, understood, and addressed in the appropriate manner. Lantern of Meridel is non-political. We believe that all American Jews, regardless of ideological belief, can embrace the concept that in order to ensure the survival of the Jewish people there must be Jewish people. At the annual Passover Seder we say that "in every generation they stand ready to annihilate us" - this is both historically accurate and currently relevant.</p>
  <a class="pill btn-small btn-blue" style="left:222px;top:941px">READ MORE
    <svg class="arrow" width="16" height="16" viewBox="0 0 19 19"><circle cx="9.5" cy="9.5" r="8.5" fill="none" stroke="#fff" stroke-width="1.4"/><path d="M7 6l3.5 3.5L7 13M10 6l3.5 3.5L10 13" stroke="#fff" stroke-width="1.4" fill="none"/></svg></a>
  <div class="mission-frame"></div>
  <div class="mission-photo" role="img" aria-label="Smiling woman pointing, set on a blue and red backdrop"></div>

  <!-- pillars -->
  <svg class="pillar-map" viewBox="330 1070 540 370">
    <polygon points="599,1142 691,1195 691,1301 599,1354 507,1301 507,1195" fill="none" stroke="var(--red)" stroke-width="1.5"/>
    <polygon points="599,1156 680,1202 680,1294 599,1340 518,1294 518,1202" fill="var(--blue)"/>
    <g stroke="var(--blue)" stroke-width="1.5">
      <line x1="599" y1="1142" x2="599" y2="1102"/>
      <line x1="599" y1="1354" x2="599" y2="1394"/>
      <line x1="699" y1="1195" x2="738" y2="1175"/>
      <line x1="699" y1="1301" x2="738" y2="1321"/>
      <line x1="499" y1="1195" x2="462" y2="1177"/>
      <line x1="499" y1="1301" x2="462" y2="1320"/>
    </g>
    <g fill="var(--blue)">
      <circle cx="599" cy="1146" r="3.5"/><circle cx="599" cy="1350" r="3.5"/>
      <circle cx="699" cy="1195" r="3.5"/><circle cx="699" cy="1301" r="3.5"/>
      <circle cx="499" cy="1195" r="3.5"/><circle cx="499" cy="1301" r="3.5"/>
    </g>
  </svg>
  <div class="hex-name">LANTERN OF MERIDEL</div>
  <div class="pillar-label" style="left:569px;top:1081px;width:60px">PRIDE</div>
  <div class="pillar-label" style="left:715px;top:1158px;width:100px">ASSIMILATION</div>
  <div class="pillar-label" style="left:360px;top:1162px;width:120px">GROWING ANTI<br>SEMITISM</div>
  <div class="pillar-label" style="left:344px;top:1313px;width:140px">ISRAEL IS THE<br>JEWISH HOMELAND</div>
  <div class="pillar-label" style="left:730px;top:1328px;width:40px">BDS</div>
  <div class="pillar-label" style="left:499px;top:1405px;width:200px">ISRAEL MUST RETAIN ITS<br>TRUE TRADITION JEWISH</div>

  <!-- objectives -->
  <h2 class="section-title" style="left:222px;top:1503px">OBJECTIVES</h2>

  <article class="card" style="left:222px;top:1566px">
    <h3>Resist Assimilation</h3>
    <p>Assimilation is an issue facing every religion. With respect to Judaism, Lantern of Meridel underscores the need for education regarding our history, heritage and the beauty of Judaism.</p>
    <a class="btn-card">DISCOVER MORE</a>
  </article>
  <article class="card featured" style="left:478px;top:1566px">
    <h3>Confront Anti-Semitism</h3>
    <p>Anti-Semitism in America is unfortunately, becoming the new norm. While the attacks against Jews in Pittsburgh and California garnered a lot of media attention, there are ever-increasing incidents of hate crimes against the Jewish people in the U.S</p>
    <a class="btn-card">DISCOVER MORE</a>
  </article>
  <article class="card" style="left:735px;top:1566px">
    <h3>Expose BDS</h3>
    <p>BDS has not yet gained enough traction to be a real threat currently, but the threat of BDS looms large when considering the left-leaning American college environment. In twenty years, today's college students who are being inculcated by BDS will inevitably rise in local politics, Congress, or even national office.</p>
    <a class="btn-card">DISCOVER MORE</a>
  </article>
  <article class="card" style="left:222px;top:1792px">
    <h3>Instill Jewish Pride</h3>
    <p>Due to the atmosphere on many if not most of our American college campuses, students are ashamed or scared to state that they are Jewish, or that they support Israel. We must be allowed to stand tall and proud on college campuses when we identify as Jews and support Israel.</p>
    <a class="btn-card">DISCOVER MORE</a>
  </article>
  <article class="card" style="left:478px;top:1792px">
    <h3>Israel: The Eternal Jewish Homeland</h3>
    <p>For thousands of years, Judaism has been inextricably bound with Israel. Since 1948, Israel has been a Jewish State based on its original deed – the Torah that was given to us at Mount Sinai, as well as worldwide recognition of the Jewish right to Israel as a homeland. This is a mandate that must be protected</p>
    <a class="btn-card">DISCOVER MORE</a>
  </article>
  <article class="card" style="left:735px;top:1792px">
    <h3>Maintain Israel's Jewish Identity</h3>
    <p>While Lantern of Meridel recognizes that Jews are empowered with free choice, particularly in their beliefs and levels of ritual observance, it also recognizes that for Israel to maintain its standing as a Jewish State it must institutionally retain its TRUE TRADITIONAL Jewish Identity</p>
    <a class="btn-card">DISCOVER MORE</a>
  </article>

  <!-- voting -->
  <div class="vote-band"></div>
  <h2 class="vote-title">OUR VOTING PROCESS</h2>
  <div class="vote-video" role="img" aria-label="Video still of students in a classroom raising hands to vote"></div>
  <svg class="play" width="78" height="78" viewBox="0 0 78 78"><circle cx="39" cy="39" r="35" fill="none" stroke="#fff" stroke-width="5"/><polygon points="31,23 56,39 31,55" fill="#fff"/></svg>

  <!-- join form -->
  <section class="join"></section>
  <h2 class="join-title">JOIN THE JEWISH FUTURE</h2>
  <p class="join-sub">Help us ensure a world Jewish platform that keeps our people and communities strong, safe and proud.</p>
  <div class="field" style="left:222px;top:2636px;width:372px;height:36px">FULL NAME</div>
  <div class="field" style="left:603px;top:2636px;width:374px;height:36px">E-MAIL</div>
  <div class="field" style="left:222px;top:2688px;width:372px;height:36px">PHONE</div>
  <div class="field" style="left:603px;top:2688px;width:374px;height:36px">CITY</div>
  <div class="field msg" style="left:220px;top:2740px;width:759px;height:95px">MESSAGE</div>
  <a class="pill btn-red btn-vote">GO OUT TO VOTE
    <svg width="18" height="16" viewBox="0 0 18 16"><path d="M1 7L17 1 13 15 9 10 6 14 6 9 15 3 5 8Z" fill="#fff"/></svg></a>

  <!-- footer -->
  <svg class="footer-wave" viewBox="0 0 1200 142">
    <path d="M880,40 C1040,12 1150,4 1200,0 V60 Z" fill="var(--blue-light)"/>
    <path d="M0,10 C150,35 320,80 520,80 C720,78 920,45 1200,5 V80 C900,70 700,100 500,110 C300,118 150,100 0,70 Z" fill="var(--blue-mid)"/>
    <path d="M0,60 C150,110 300,125 460,112 C700,85 950,28 1200,20 V142 H0 Z" fill="#000"/>
  </svg>
  <footer class="footer"></footer>
  <div class="footer-brand">LANTERN OF MERIDEL</div>
  <a class="footer-link" style="left:370px">HOME</a>
  <a class="footer-link" style="left:457px">MISSION STATEMENT</a>
  <a class="footer-link" style="left:620px">OBJECTIVES<svg class="chev" width="9" height="6" viewBox="0 0 9 6"><path d="M1 1l3.5 3.5L8 1" stroke="#fff" stroke-width="1.4" fill="none"/></svg></a>
  <a class="footer-link" style="left:764px">CONTACT US</a>
  <div class="footer-rule"></div>
  <div class="copyright">Copyright © 2020 Lantern of Meridel &nbsp;|&nbsp; Privacy Policy</div>

</div>
</body>
</html>
```